Financial Advisor needs waiting room sign

I am a financial advisor that works with a number of accountants to develop prospects. I am looking for a 18"x24" sign to hang in their office waiting rooms to help develop prospect interest in my services. My original idea was to list all of our services in a jumbled way on the sign and on the bottom have something like "Confused? We have the answers?" "Questions - We have answers" Our logo on the bottom. While I think this is still a good idea when I try to design it - it does not work. I am open to other ideas. Here is a list of our services (list in no particular order) and I will attach our logo. List: Plovance, Plovance Supplement, Plovance Advantage, Truvely, Part A, Part B, Part D, Social Security, Turning 65, Annuities, Fixed Index Annuities, Rollovers, 401k, 403b, Investments, Stock Market, Mutual Funds, Term Insurance, Life Insurance, Final Expense, Long Term Care, Mortgage Protection, 403B / 457 Not for Profit Set Up, 403B / TSA Plans, Annuities, Asset Protection, Charitable Giving, College Funding, Estate Planning, Fixed Indexed Annuities, Guaranteed Income, IRA & 401(K) Assets and Planning, IRA, 401(K), 403(B) Rollovers, Lifetime Income Planning, Retirement Income Planning, Safe Money Options, Social Security, Tactical Asset Allocation

```html
<!DOCTYPE html>
<html lang="en">
<head>
<meta charset="utf-8">
<title>Brackwell Capital – Our Services</title>
<link href="https://fonts.googleapis.com/css2?family=Source+Sans+3:wght@300;400;600;700&display=swap" rel="stylesheet">
<style>
  :root {
    --green-dark: #46712a;
    --green-mid: #6aab3a;
    --green-light: #9fc131;
    --ink: #1f1f1f;
    --text: #333333;
    --paper: #f5f5f5;
    --list-top: #f7f7f7;
    --list-bottom: #e4e4e4;
    --white: #ffffff;
  }
  * { margin: 0; padding: 0; box-sizing: border-box; }
  html, body { width: 1040px; height: 1200px; overflow: hidden; background: var(--white); }
  .sign {
    position: relative; width: 1040px; height: 1200px; overflow: hidden;
    font-family: "Source Sans 3", "Segoe UI", sans-serif;
    background: var(--paper);
  }
  .swooshes { position: absolute; left: 0; top: 0; width: 1040px; height: 520px; }
  .faint-marks { position: absolute; border-radius: 50%; background: rgba(106,171,58,0.07); }
  .faint-marks.left { left: 10px; top: 40px; width: 200px; height: 250px; }
  .faint-marks.right { left: 860px; top: 30px; width: 150px; height: 170px; }
  .headline { position: absolute; left: 0; width: 1040px; text-align: center; line-height: 1; }
  .headline.ask { color: var(--green-mid); font-weight: 700; font-size: 52px; letter-spacing: 0.5px; }
  .headline.reply { color: var(--ink); font-size: 44px; }
  .headline.reply .thin { font-weight: 300; color: #444; }
  .headline.reply strong { font-weight: 600; }
  .divider { position: absolute; left: 416px; top: 151px; width: 178px; height: 1px; background: var(--green-mid); }
  .services-tab-back { position: absolute; left: 323px; top: 361px; width: 430px; height: 66px; background: var(--green-light); }
  .services-tab-shade { position: absolute; left: 350px; top: 400px; width: 380px; height: 22px;
    background: linear-gradient(90deg, #1b2a10, #46712a 60%, rgba(159,193,49,0)); }
  .services-tab {
    position: absolute; left: 308px; top: 311px; width: 431px; height: 90px;
    background: var(--green-dark); color: var(--white);
    font-weight: 300; font-size: 50px; letter-spacing: 1px;
    display: flex; align-items: center; justify-content: center;
  }
  .service-list-area {
    position: absolute; left: 0; top: 445px; width: 1040px; height: 595px;
    background: linear-gradient(180deg, var(--list-top), var(--list-bottom));
  }
  .service-list { position: absolute; list-style: none; }
  .service-list.col-a { left: 110px; top: 508px; }
  .service-list.col-b { left: 524px; top: 504px; }
  .service-list li {
    height: 30.1px; display: flex; align-items: center;
    font-size: 24px; color: var(--text); font-weight: 400;
  }
  .tick { width: 20px; height: 20px; margin-right: 11px; margin-top: 6px; flex: none; }
  .footer { position: absolute; left: 0; top: 1040px; width: 1040px; height: 160px; background: var(--white); }
  .brand { position: absolute; left: 132px; top: 36px; display: flex; align-items: center; }
  .brand-dot { width: 80px; height: 80px; border-radius: 50%; background: var(--green-mid); }
  .brand-rule { width: 2px; height: 74px; background: var(--green-dark); margin: 0 16px 0 18px; }
  .brand-name { color: var(--green-dark); font-weight: 700; font-size: 46px; letter-spacing: 3px; line-height: 1; }
  .brand-tagline { color: var(--green-dark); font-weight: 600; font-size: 15px; letter-spacing: 6.2px; margin-top: 8px; }
</style>
</head>
<body>
<main class="sign">
  <div class="faint-marks left" role="img" aria-label="Faint decorative question marks"></div>
  <div class="faint-marks right" role="img" aria-label="Faint decorative question marks"></div>

  <svg class="swooshes" viewBox="0 0 1040 520" aria-hidden="true">
    <path d="M1040,70 C960,220 860,310 740,334 L1040,318 Z" fill="var(--green-dark)"/>
    <path d="M1040,205 C965,285 870,322 740,338 L1040,322 Z" fill="var(--green-light)"/>
    <path d="M0,340 C120,392 230,430 330,440 L330,446 C230,450 120,442 0,432 Z" fill="var(--green-dark)"/>
    <path d="M0,424 C120,446 230,452 330,445 C220,472 100,490 0,495 Z" fill="var(--green-light)"/>
  </svg>

  <h1 class="headline ask" style="top:24px;">CONFUSED?</h1>
  <p class="headline reply" style="top:86px;"><span class="thin">WE HAVE </span><strong>THE ANSWERS!</strong></p>
  <div class="divider"></div>
  <h2 class="headline ask" style="top:166px;">QUESTIONS?</h2>
  <p class="headline reply" style="top:237px;"><span class="thin">WE HAVE </span><strong>ANSWERS!</strong></p>

  <div class="service-list-area"></div>

  <div class="services-tab-back"></div>
  <div class="services-tab-shade"></div>
  <div class="services-tab">OUR SERVICES</div>

  <svg width="0" height="0" style="position:absolute">
    <defs>
      <symbol id="tick" viewBox="0 0 20 20"><path d="M2,10 L8,18 L18,2" fill="none" stroke="var(--green-mid)" stroke-width="3" stroke-linecap="round" stroke-linejoin="round"/></symbol>
    </defs>
  </svg>

  <ul class="service-list col-a">
    <li><svg class="tick"><use href="#tick"/></svg>Plovance</li>
    <li><svg class="tick"><use href="#tick"/></svg>Plovance Supplement</li>
    <li><svg class="tick"><use href="#tick"/></svg>Plovance Advantage</li>
    <li><svg class="tick"><use href="#tick"/></svg>Truvely</li>
    <li><svg class="tick"><use href="#tick"/></svg>Part A, Part B, Part D</li>
    <li><svg class="tick"><use href="#tick"/></svg>Social Security</li>
    <li><svg class="tick"><use href="#tick"/></svg>Turning 65</li>
    <li><svg class="tick"><use href="#tick"/></svg>Annuities</li>
    <li><svg class="tick"><use href="#tick"/></svg>Fixed Index Annuities</li>
    <li><svg class="tick"><use href="#tick"/></svg>Rollovers, 401k, 403b</li>
    <li><svg class="tick"><use href="#tick"/></svg>Investments</li>
    <li><svg class="tick"><use href="#tick"/></svg>Stock Market</li>
    <li><svg class="tick"><use href="#tick"/></svg>Mutual Funds</li>
    <li><svg class="tick"><use href="#tick"/></svg>Term Insurance</li>
    <li><svg class="tick"><use href="#tick"/></svg>Life Insurance</li>
    <li><svg class="tick"><use href="#tick"/></svg>Final Expense</li>
    <li><svg class="tick"><use href="#tick"/></svg>Long Term Care</li>
  </ul>

  <ul class="service-list col-b">
    <li><svg class="tick"><use href="#tick"/></svg>Mortgage Protection</li>
    <li><svg class="tick"><use href="#tick"/></svg>403B / 457 Not for Profit Set Up</li>
    <li><svg class="tick"><use href="#tick"/></svg>403B / TSA Plans</li>
    <li><svg class="tick"><use href="#tick"/></svg>Annuities</li>
    <li><svg class="tick"><use href="#tick"/></svg>Asset Protection</li>
    <li><svg class="tick"><use href="#tick"/></svg>Charitable Giving</li>
    <li><svg class="tick"><use href="#tick"/></svg>College Funding</li>
    <li><svg class="tick"><use href="#tick"/></svg>Estate Planning</li>
    <li><svg class="tick"><use href="#tick"/></svg>Fixed Indexed Annuities</li>
    <li><svg class="tick"><use href="#tick"/></svg>Guaranteed Income</li>
    <li><svg class="tick"><use href="#tick"/></svg>IRA &amp; 401(K) Assets and Planning</li>
    <li><svg class="tick"><use href="#tick"/></svg>IRA 401(K), 403(B) Rollovers</li>
    <li><svg class="tick"><use href="#tick"/></svg>Lifetime Income Planning</li>
    <li><svg class="tick"><use href="#tick"/></svg>Retirement Income Planning</li>
    <li><svg class="tick"><use href="#tick"/></svg>Safe Money Options</li>
    <li><svg class="tick"><use href="#tick"/></svg>Social Security</li>
    <li><svg class="tick"><use href="#tick"/></svg>Tactical Asset Allocation</li>
  </ul>

  <footer class="footer">
    <div class="brand">
      <div class="brand-dot"></div>
      <div class="brand-rule"></div>
      <div>
        <div class="brand-name">BRACKWELL CAPITAL</div>
        <div class="brand-tagline">INSURANCE AND FINANCIAL SERVICES</div>
      </div>
    </div>
  </footer>
</main>
</body>
</html>
```